Brookline Wealth Guidance - Employer Benefit Brochure

We need to design a professional looking brochure that we can present to our existing client base, and assist in attracting new clients.
The current information is just provided in a word document, but we need to improve significantly.
The audience would be business leaders, HR decision makers and member policy committee members

Industry/Entity Type

Business

Font styles to use
Sans Serif

Colors
0255a3
f37122

```html
<!DOCTYPE html>
<html lang="en">
<head>
<meta charset="utf-8">
<title>Brookline Wealth Guidance – Employer Benefit Brochure</title>
<link rel="stylesheet" href="https://fonts.googleapis.com/css2?family=Questrial&display=swap">
<style>
  :root {
    --brand-blue: #0255a3;
    --heading-blue: #1a3fd6;
    --brand-orange: #f37122;
    --body-text: #333333;
    --page: #ffffff;
    --backdrop: #e9e7e3;
    --folio: #3a3f42;
    --badge-blue: #5ec7ef;
    --photo-sky: #3a78c9;
    --photo-sky-light: #6ea4e2;
    --photo-table: #8a5a36;
    --photo-table-dark: #5b3a22;
  }
  * { box-sizing: border-box; margin: 0; padding: 0; }
  html, body { width: 1200px; height: 859px; overflow: hidden; }
  body {
    background: var(--backdrop);
    font-family: "Questrial", "Century Gothic", sans-serif;
    color: var(--body-text);
    position: relative;
  }
  .spread {
    position: absolute; left: 38px; top: 30px;
    width: 1124px; height: 799px;
    background: var(--page);
  }
  .accent-bar { position: absolute; top: 53px; width: 14px; height: 665px; }
  .accent-bar--left { left: 28px; background: var(--brand-orange); }
  .accent-bar--right { left: 1082px; background: var(--brand-blue); }
  .feature-photo {
    position: absolute; left: 346px; top: 0; width: 431px; height: 799px;
    background: linear-gradient(180deg, var(--photo-sky-light) 0%, var(--photo-sky) 45%, var(--photo-sky) 60%, var(--photo-table) 68%, var(--photo-table-dark) 100%);
  }
  .section { position: absolute; }
  .section h2 {
    font-weight: 400; font-size: 24px; line-height: 28px;
    letter-spacing: -0.2px;
  }
  .section h2.blue { color: var(--heading-blue); }
  .section h2.orange { color: var(--brand-orange); }
  .section p {
    font-size: 9.6px; line-height: 11.6px; text-align: justify;
    margin-bottom: 11.6px;
  }
  .partner-name {
    display: flex; align-items: center; gap: 6px;
    font-size: 20px; color: var(--brand-blue);
  }
  .partner-name .mark { width: 26px; height: 26px; background: var(--brand-blue); border-radius: 50%; }
  .partner-name .mark--square { width: 56px; height: 42px; border-radius: 0; background: var(--badge-blue); }
  .partner-name--small { font-size: 13px; }
  .icon-slot { background: #cfcfcf; }
  .bullets p { margin-bottom: 11.6px; }
  .folio {
    position: absolute; top: 744px; width: 33px; height: 33px; border-radius: 50%;
    background: var(--folio); color: #fff; font-size: 13px;
    display: flex; align-items: center; justify-content: center;
  }
</style>
</head>
<body>
<main class="spread">
  <div class="accent-bar accent-bar--left"></div>

  <section class="section health" style="left:58px; top:78px; width:266px;">
    <h2 class="blue">Health Insurance</h2>
    <div class="partner-name" style="margin:6px 0 16px;"><span class="mark"></span>Meridian Health</div>
    <p>We believe that investing in employee health and well-being can have a positive contribution on your bottom line and enhance your employee's engagement. Brookline's partner is Meridian Health, Australia's only corporate health insurance specialist, focused solely on providing innovative health insurance products and services to businesses.</p>
    <p>Meridian Health's corporate health insurance is all they do. Unlike retail health funds they understand that no two businesses are alike and they design a health insurance plan to be unique to the business.</p>
    <p>Servicing over 300 companies, they apply their expert private health insurance knowledge so that a client is not forced into a one-size-fits-all solution. We work together to ensure your the health plan is tailored to the industry, budget, payroll structures and employee profile.</p>
    <p>Partnering through Brookline with Meridian Health will ensure you get more from the investment in your most important resource — your people. Meridian Health can work with you to tailor a solution that will make a tangible difference to employee engagement and productivity.</p>
  </section>

  <section class="section travel" style="left:58px; top:455px; width:266px;">
    <h2 class="orange">Travel Insurance</h2>
    <div class="partner-name partner-name--small" style="margin:9px 0 18px;"><span class="mark mark--square"></span>Harbourline</div>
    <p>Brookline's partner, Harbourline Travel Cover, has a comprehensive range of corporate travel insurance policies to meet all business needs and provides the cover that is optimal for your business and your budget.</p>
    <p>Harbourline are able to tailor a solution to meet your business needs and offer a 24/7 emergency assistance team.</p>
  </section>

  <div class="folio" style="left:261px;">9</div>

  <div class="feature-photo" role="img" aria-label="Photograph of two cupped hands sheltering a paper-cut family of four standing on a wooden table against a blue backdrop"></div>

  <section class="section key-person" style="left:792px; top:78px; width:276px;">
    <h2 class="blue">Key Person Insurance</h2>
    <div class="icon-slot" role="img" aria-label="Small umbrella icon" style="width:42px; height:34px; margin:8px 0 10px;"></div>
    <p>Brookline offers business advice and solutions for Key Person insurance. Often overlooked, this is an important financial risk mitigation tool during the prolonged absence or death of a key employee.</p>
    <p>Below are the categories of loss in which a Key Person insurance policy can provide the business with financial security:</p>
    <div class="bullets">
      <p>• Covers the costs of hiring temporary personnel or if necessary, for the recruitment and training of a replacement.</p>
      <p>• Protect your cash flow and profits (e.g. when a business project involving the key person is cancelled or when the loss of the key person amounts to lost sales and income).</p>
      <p>• Provides cover in instances whereby you lose a person involved in guaranteeing banking facilities or business loans.</p>
      <p>• Finally, partnership interests or shareholders may be protected by allowing other existing partners or shareholders to purchase the shareholdings.</p>
    </div>
  </section>

  <section class="section asset-finance" style="left:792px; top:438px; width:276px;">
    <h2 class="orange">Asset and Equipment<br>Finance <span class="icon-slot" role="img" aria-label="Small key with leasing tag icon" style="display:inline-block; width:42px; height:22px; vertical-align:middle; margin-left:4px;"></span></h2>
    <p style="margin-top:12px;">Our finance partner, Keystone Asset Finance (KAF), provides both you and your employees specialist support in the areas of motor vehicle and equipment finance and novated and general leasing.</p>
    <p style="margin-bottom:0;">Dealing with employees seeking the right motor vehicle options takes time. Explaining and getting the right finance takes experience. KAF provides an end to end solution from finding the right motor vehicle to sourcing the right motor vehicle/capital equipment finance and arranging the documentation with HR and your payroll provider.</p>
    <p>KAF assists you access a full suite of business related finance products, as well as employee funding options for cars, boats and motor cycles.</p>
    <p>KAF also provides employees looking for a new car with access to Fleet Prices across any dealer network. This means they can find the right car and can negotiate a better price than is ordinarily available to the general public, and arrange the appropriate finance.</p>
  </section>

  <div class="folio" style="left:823px;">10</div>

  <div class="accent-bar accent-bar--right"></div>
</main>
</body>
</html>
```